BRVL web site redesign

Coastal Linkwork Systems service (BRVL) is a diverse technology company specialising in design and installation of fibre optics, network convergence and building services, for commercial clients in Australia, we required a new design of our website to attract new clients, generate sales leads, and provide information about our services to the market. The site and should have a new technology look and feel and be designed in word press. our branding colour is blue.

Target Market(s)

New developments, Construction organisations, Commercial end users, IT managers, Consultants.

Industry/Entity Type

It Company

Number of Pages Required

5+ page

Font styles to use
Sans Serif

Colors
0292cd
3176b5

Requirements
Must have
• key pages.
• Home page with some sizzle, automated pictures running through, I like the look of this competitor website http://www.tarelmesh.com.au/ good clean menus and easy to navigate.
• Services page our key services are Fibre optics, Security, Building services,Electrical. I would like the same page layout (Design) for all our services, with a find out more link on each page, manly picture driven with text around our key messaging.
• About us page with space for company profile and directors pictures, bio and contact information.
• Certifications / Accreditations page with have over 20 certifications on different products from suppliers, and a number of licences from governing bodies.
• Current and past projects page with case studies and customer outcomes
• Contact us page with options around what services they require more information on, please keep in mind the site is around generating sales Leeds and being seen as an industry expert.
Nice to have
• RSS feeds, Linked in link, to be placed within the design, Consistent BRVL branding,Same colour blue as our logo Document library for education information, white papers, presentations etc,
• a new technology look and feel, mobile friendly.
Should not have
• boring layout, move away from our cuurent website http://www.brvlgroup.com.au/
• no e eCommerce store required.

```html
<!DOCTYPE html>
<html lang="en">
<head>
<meta charset="utf-8">
<title>BRVL – Coastal Linkwork Systems Service</title>
<link rel="stylesheet" href="https://fonts.googleapis.com/css2?family=Josefin+Sans:wght@300;400;600&family=Open+Sans:wght@400;600&display=swap">
<style>
:root{
  --blue:#0292cd;
  --blue-deep:#3176b5;
  --blue-nav:#1679b3;
  --ink:#444b52;
  --muted:#777d83;
  --ring:#a8abae;
  --band:#dfe5ea;
  --footer:#243a46;
  --footer-text:#c8d2d8;
  --bottom:#1f2326;
  --white:#ffffff;
}
*{box-sizing:border-box;margin:0;padding:0}
html,body{width:727px;height:1200px;overflow:hidden}
body{position:relative;background:var(--white);font-family:"Open Sans",Arial,sans-serif;color:var(--ink)}
.abs{position:absolute}

/* header */
.brand{left:76px;top:7px;width:97px;height:37px;background:var(--blue);display:flex;align-items:center;justify-content:center;gap:6px}
.brand-name{font-family:"Josefin Sans",sans-serif;font-weight:600;font-size:24px;color:var(--white);letter-spacing:1px;padding-top:4px}
.brand-mark{width:9px;height:9px;background:var(--white)}
.top-contact{right:76px;top:7px;display:flex;align-items:center;gap:10px;font-size:10px;color:var(--ink)}
.top-contact svg{display:block}
.site-title{right:76px;top:22px;font-family:"Josefin Sans",sans-serif;font-weight:300;font-size:20px;color:var(--ink)}
.main-nav{left:73px;top:48px;width:579px;height:19px;background:var(--blue-nav);display:flex;align-items:center;padding-left:2px}
.main-nav a{color:var(--white);text-decoration:none;font-size:9px;padding:0 9px;height:19px;line-height:19px;text-transform:uppercase;border-right:1px solid rgba(255,255,255,.35)}
.main-nav a:first-child{text-transform:none;background:#0f6aa0}
.nav-search{position:absolute;right:3px;top:3px;display:flex}
.nav-search span{width:80px;height:13px;background:var(--white)}
.nav-search i{width:14px;height:13px;background:var(--white);margin-left:2px;display:flex;align-items:center;justify-content:center}

/* hero */
.hero{left:0;top:71px;width:727px;height:297px;background:linear-gradient(90deg,#6b7f8c 0%,#a9b8c2 25%,#dfe4e8 45%,#eef0f2 70%,#dfe3e6 100%)}
.hero-card{left:76px;top:156px;width:317px;height:117px;background:rgba(25,35,45,.72);padding:10px 12px}
.hero-card h1{font-family:"Josefin Sans",sans-serif;font-weight:400;font-size:16.5px;letter-spacing:-.2px;color:var(--blue);line-height:1.1;white-space:nowrap}
.hero-card p{font-size:8.5px;color:#e6ecef;line-height:1.45;margin-top:5px;width:290px}
.hero-btn{display:inline-flex;align-items:center;gap:14px;margin-top:10px;background:var(--blue-nav);color:var(--white);font-size:12px;padding:5px 10px;font-family:"Josefin Sans",sans-serif}

/* what we do */
.section-title{left:0;width:727px;top:386px;text-align:center;font-family:"Josefin Sans",sans-serif;font-weight:300;font-size:20px;color:var(--ink)}
.section-title b{font-weight:400;color:var(--blue);font-size:25px}
.intro{left:100px;top:416px;width:527px;text-align:center;font-size:8.4px;line-height:1.5;color:var(--muted)}
.services-line{left:0;top:470px}
.service{width:140px;text-align:center;top:482px}
.service svg{display:block;margin:0 auto}
.service p{font-size:9.5px;color:var(--ink);line-height:1.35;margin-top:6px}

/* grid */
.band{left:0;top:634px;width:727px;height:320px;background:linear-gradient(180deg,#eef1f4,#d7dee4)}
.tile{width:183px;height:116px;display:flex;align-items:center;justify-content:center;text-align:center;color:var(--white);font-family:"Josefin Sans",sans-serif;font-weight:400;font-size:14px;line-height:1.15;border:1px solid rgba(255,255,255,.6)}
.t1{background:linear-gradient(160deg,#6f6a5f,#3c3f41)}
.t2{background:linear-gradient(160deg,#8a98a6,#4a5663)}
.t3{background:linear-gradient(160deg,#2f4a63,#1a2632)}
.t4{background:linear-gradient(160deg,#6c5b4e,#3a3d45)}
.t5{background:linear-gradient(160deg,#4f6676,#233440)}
.t6{background:linear-gradient(160deg,#7e8a93,#4b565f)}

/* newsletter */
.newsletter{left:133px;top:934px;width:450px;height:40px;background:var(--blue-nav);display:flex;align-items:center;padding:0 14px;gap:14px}
.newsletter h2{font-family:"Open Sans",sans-serif;font-weight:600;font-size:16px;color:var(--white)}
.newsletter h2 span{color:#0d2c44}
.newsletter .field{width:168px;height:21px;background:var(--white)}
.newsletter .send{width:27px;height:21px;background:#0d2c44;display:flex;align-items:center;justify-content:center}

/* footer */
.footer{left:0;top:954px;width:727px;height:200px;background:var(--footer)}
.col{top:1008px;color:var(--footer-text)}
.col h3{font-weight:400;font-size:10px;color:var(--white);text-transform:uppercase;margin-bottom:12px}
.col h3.plain{text-transform:none}
.tweet{display:flex;gap:8px;font-size:6.6px;line-height:1.5;width:150px;margin-bottom:8px}
.tweet .dot{flex:none;width:5px;height:5px;border-radius:50%;background:var(--blue);margin-top:2px}
.tweet b{font-weight:600;color:var(--blue)}
.links li{list-style:none;font-size:6.6px;padding:5px 0 5px 14px;border-bottom:1px solid rgba(255,255,255,.12);position:relative;width:115px}
.links li::before{content:"›";position:absolute;left:2px;top:2px;font-size:10px;color:#7f8f99}
.contact li{list-style:none;display:flex;gap:8px;font-size:6.6px;margin-bottom:12px;width:130px;line-height:1.5}
.contact b{font-weight:600;color:var(--white)}
.bottom{left:0;top:1154px;width:727px;height:46px;background:var(--bottom);display:flex;align-items:center;justify-content:space-between;padding:0 76px;font-size:7.5px;color:#b8c0c5}
.social{display:flex;gap:6px}
.social span{width:20px;height:20px;border-radius:50%}
</style>
</head>
<body>

<header>
  <div class="abs brand"><span class="brand-name">BRVL</span><span class="brand-mark"></span></div>
  <div class="abs top-contact">
    <svg width="10" height="9" viewBox="0 0 10 9"><path d="M5 0 0 4.5h1.5V9h2.5V6h2v3h2.5V4.5H10z" fill="var(--blue-nav)"/></svg>
    <svg width="9" height="9" viewBox="0 0 9 9"><path d="M2 0 3.5 2.5 2.5 3.6q1 2 3 3l1.1-1L9 7 7.6 9Q3.5 8.5 0 1.4z" fill="var(--blue-nav)"/></svg>
    <span>1300 555 246</span>
  </div>
  <div class="abs site-title">Coastal Linkwork Systems Service</div>
  <nav class="abs main-nav">
    <a>BRVL Group</a><a>About us</a><a>Services</a><a>ISP</a><a>Recent projects</a><a>Contact us</a><a>Blog</a>
    <div class="nav-search"><span></span><i><svg width="8" height="8" viewBox="0 0 8 8"><circle cx="3.2" cy="3.2" r="2.4" fill="none" stroke="var(--blue-nav)" stroke-width="1.2"/><path d="M5 5l2.5 2.5" stroke="var(--blue-nav)" stroke-width="1.3"/></svg></i></div>
  </nav>
</header>

<section class="abs hero" role="img" aria-label="Photo of a technician in a suit working on a laptop beside a server rack with patch cables"></section>
<div class="abs hero-card">
  <h1>Know your shopper Know your store</h1>
  <p>We deliver Measurable Consumer Engagements in your locations. That ignite your Brand experience in your locations and connect with customers through targeted digital engagements.</p>
  <span class="hero-btn">Get Start Now <svg width="10" height="9" viewBox="0 0 10 9"><path d="M1 1l3.5 3.5L1 8M5 1l3.5 3.5L5 8" fill="none" stroke="#fff" stroke-width="1.3"/></svg></span>
</div>

<h2 class="abs section-title">What We Do <b>Tovrin</b></h2>
<p class="abs intro">BRVL is diversified technology company 100% Australian owned and operated, we provide Communication, Electrical, Security &amp; ICT services for residential and commercial customers. With over 100 years of combined industry knowledge we pride ourselves on innovated solutions that utilises technology advancements which delivers on our customer's expectations.</p>

<svg class="abs services-line" width="727" height="130" viewBox="0 0 727 130">
  <path d="M151 80 Q221 100 291 80 T431 80 T571 80" fill="none" stroke="#8fd3ee" stroke-width="1.2" stroke-dasharray="2 3"/>
</svg>

<div class="abs service" style="left:81px">
  <svg width="104" height="104" viewBox="0 0 104 104">
    <circle cx="52" cy="52" r="46" fill="none" stroke="var(--ring)" stroke-width="10"/>
    <path d="M52 6a46 46 0 0 1 46 46" fill="none" stroke="#d3d5d7" stroke-width="10"/>
    <circle cx="52" cy="52" r="36" fill="#f3f4f5"/>
    <g fill="var(--blue-nav)" stroke="var(--blue-nav)" stroke-width="2">
      <line x1="52" y1="52" x2="32" y2="60"/><line x1="52" y1="52" x2="72" y2="60"/><line x1="52" y1="52" x2="52" y2="74"/>
      <circle cx="52" cy="42" r="6"/><path d="M42 56q10-10 20 0z"/>
      <circle cx="30" cy="61" r="4"/><circle cx="74" cy="61" r="4"/><circle cx="52" cy="76" r="4"/>
    </g>
  </svg>
  <p>Commercial Security<br>Systems</p>
</div>
<div class="abs service" style="left:221px">
  <svg width="104" height="104" viewBox="0 0 104 104">
    <circle cx="52" cy="52" r="46" fill="none" stroke="var(--ring)" stroke-width="10"/>
    <path d="M52 6a46 46 0 0 1 46 46" fill="none" stroke="#d3d5d7" stroke-width="10"/>
    <circle cx="52" cy="52" r="36" fill="#f3f4f5"/>
    <rect x="33" y="38" width="32" height="32" fill="none" stroke="var(--blue-nav)" stroke-width="5"/>
    <path d="M47 57l20-20 5 5-20 20-7 2z" fill="var(--blue-nav)" stroke="#f3f4f5" stroke-width="2"/>
  </svg>
  <p style="margin-top:14px">Data &amp; Fibre Installations</p>
</div>
<div class="abs service" style="left:361px">
  <svg width="104" height="104" viewBox="0 0 104 104">
    <circle cx="52" cy="52" r="46" fill="none" stroke="var(--ring)" stroke-width="10"/>
    <path d="M52 6a46 46 0 0 1 46 46" fill="none" stroke="#d3d5d7" stroke-width="10"/>
    <circle cx="52" cy="52" r="36" fill="#f3f4f5"/>
    <rect x="34" y="34" width="36" height="36" rx="2" fill="none" stroke="var(--blue-nav)" stroke-width="4"/>
    <rect x="40" y="46" width="10" height="18" fill="none" stroke="var(--blue-nav)" stroke-width="3"/>
    <rect x="54" y="46" width="12" height="18" fill="none" stroke="var(--blue-nav)" stroke-width="3"/>
    <line x1="36" y1="41" x2="68" y2="41" stroke="var(--blue-nav)" stroke-width="2"/>
  </svg>
  <p>Information Communica<br>tion &amp; Technology</p>
</div>
<div class="abs service" style="left:501px">
  <svg width="104" height="104" viewBox="0 0 104 104">
    <circle cx="52" cy="52" r="46" fill="none" stroke="var(--ring)" stroke-width="10"/>
    <path d="M52 6a46 46 0 0 1 46 46" fill="none" stroke="#d3d5d7" stroke-width="10"/>
    <circle cx="52" cy="52" r="36" fill="#f3f4f5"/>
    <circle cx="50" cy="54" r="18" fill="none" stroke="var(--blue-nav)" stroke-width="5"/>
    <path d="M28 66l14-16 10 10 14-20" fill="none" stroke="var(--blue-nav)" stroke-width="5"/>
    <path d="M60 38h12v12z" fill="var(--blue-nav)"/>
  </svg>
  <p style="margin-top:2px">Electrical Fit Outs</p>
</div>

<div class="abs band" role="img" aria-label="Soft blurred photo of an office interior behind the project tiles"></div>
<div class="abs tile t1" style="left:76px;top:662px" role="img" aria-label="Photo of a warehouse distribution centre">Distribution Center<br>Solutions</div>
<div class="abs tile t2" style="left:273px;top:662px" role="img" aria-label="Photo of a team meeting in front of a whiteboard">System integration</div>
<div class="abs tile t3" style="left:468px;top:662px" role="img" aria-label="Photo of a server room aisle">Deployment solution<br>service</div>
<div class="abs tile t4" style="left:76px;top:788px" role="img" aria-label="Photo of a team planning around a table from above">Project management</div>
<div class="abs tile t5" style="left:273px;top:788px" role="img" aria-label="Photo of a hand touching a digital network display">ICT infrastructure<br>security.</div>
<div class="abs tile t6" style="left:468px;top:788px" role="img" aria-label="Photo of security cameras on a wall">Surveillance &amp; Security.</div>

<footer>
  <div class="abs footer"></div>
  <div class="abs newsletter">
    <h2><span>Subscribe</span> our Newsletter</h2>
    <div class="field"></div>
    <div class="send"><svg width="13" height="12" viewBox="0 0 13 12"><path d="M0 5 13 0 10 12 6 8 11 2 4 7z" fill="#fff"/></svg></div>
  </div>

  <div class="abs col" style="left:89px">
    <h3 class="plain">Latest Tweets</h3>
    <div class="tweet"><span class="dot"></span><p>Lorem Ipsum is simply dummy text of the printing and <b>typesetting printing and typesetting industry</b></p></div>
    <div class="tweet"><span class="dot"></span><p>Lorem Ipsum is simply dummy text of the printing and <b>typesetting printing and typesetting industry</b></p></div>
  </div>
  <div class="abs col" style="left:240px">
    <h3>Services</h3>
    <ul class="links"><li>Commercial Security Systems</li><li>Data &amp; Fibre Installations</li><li>Information Communication</li><li>Electrical Fit Outs</li></ul>
  </div>
  <div class="abs col" style="left:383px">
    <h3>Information</h3>
    <ul class="links"><li>My Account</li><li>Sign In Order</li><li>Status My Cart</li><li>My Wishlist</li></ul>
  </div>
  <div class="abs col" style="left:527px">
    <h3>Contact Info</h3>
    <ul class="contact">
      <li><svg width="8" height="8" viewBox="0 0 9 9"><path d="M2 0 3.5 2.5 2.5 3.6q1 2 3 3l1.1-1L9 7 7.6 9Q3.5 8.5 0 1.4z" fill="var(--blue)"/></svg><span>Telephone : <b>+61 2 5550 1184</b></span></li>
      <li><svg width="9" height="7" viewBox="0 0 9 7"><rect width="9" height="7" fill="var(--blue)"/><path d="M0 0l4.5 4L9 0" fill="none" stroke="var(--footer)" stroke-width="1"/></svg><span>Email : <b>info@brvl.com.au</b></span></li>
      <li><svg width="7" height="10" viewBox="0 0 7 10"><path d="M3.5 10 0 4a3.5 3.5 0 1 1 7 0z" fill="var(--blue)"/><circle cx="3.5" cy="3.5" r="1.3" fill="var(--footer)"/></svg><span>Adress : <b>18 Harbour Lane level 2 wharf road Sydney</b></span></li>
    </ul>
  </div>
  <div class="abs bottom">
    <span>© Copyright all right reserved 2015 brvl.com.au</span>
    <div class="social"><span style="background:#2a9fd8"></span><span style="background:#d8352a"></span><span style="background:#3a6fa8"></span><span style="background:#ef7a1a"></span><span style="background:#cc2233"></span></div>
  </div>
</footer>

</body>
</html>
```